Clothing range for the petite modern mature woman needs a card design

We need a business card design for a new Sydney based company called plum twist. We provide clothing to the modern mature woman who finds it difficult to source clothes that do not make them look frumpy or do not fit. We have an idea we would like an apple with the peel unravelling and possibly the silhouette of a woman's body coming out of the peel. The plum twist represents the womans body shape and dressing it.

Target Market(s)

modern mature aged woman

Industry/Entity Type

Clothing

Contact Information for Business Card

abn: 41027395816
will provide email at a later date
a spiel re clothes for modern woman???

Font styles to use
Serif
Sans Serif

Requirements
Must have
• will need name - ABN -will need email address but still working on that (TBA)
Nice to have
• picture of an apple with its peel coming off and possibly the silhouette of a woman coming out. the issue a lot of women in the over 50 range have is that the clothing is very dated or makes the woman frumpy. we are providing clothes for the woman who has difficulty in finding fashionable clothes in their size.
Should not have
• don't want childlike

```html
<!DOCTYPE html>
<html lang="en">
<head>
<meta charset="utf-8">
<title>Plum Twist — Business Card</title>
<link rel="stylesheet" href="https://fonts.googleapis.com/css2?family=Questrial&display=swap">
<style>
  :root {
    --canvas: #eef0ee;
    --leaf-green: #21a034;
    --cream: #e3e4d2;
    --stone: #bcbcaa;
    --ink-light: #f3f4ea;
    --shadow: rgba(40, 60, 40, 0.14);
  }
  * { box-sizing: border-box; margin: 0; padding: 0; }
  html, body {
    width: 1200px;
    height: 900px;
    overflow: hidden;
    background: var(--canvas);
    font-family: "Questrial", "Helvetica Neue", Arial, sans-serif;
  }
  .sheet {
    width: 1200px;
    height: 900px;
    display: flex;
    align-items: center;
    justify-content: center;
    gap: 60px;
  }
  .card {
    position: relative;
    width: 520px;
    height: 300px;
    overflow: hidden;
    box-shadow: 0 10px 28px var(--shadow);
  }

  /* Front */
  .card--front { background: var(--leaf-green); color: var(--ink-light); }
  .figure-art {
    position: absolute;
    top: 0;
    right: 0;
    width: 250px;
    height: 100%;
    background:
      radial-gradient(ellipse 58% 62% at 58% 46%,
        var(--stone) 0%, var(--stone) 45%,
        rgba(188, 188, 170, 0.55) 68%,
        rgba(33, 160, 52, 0) 100%),
      linear-gradient(180deg, rgba(227, 228, 210, 0.9) 0%, rgba(227, 228, 210, 0) 14%,
        rgba(227, 228, 210, 0) 86%, rgba(227, 228, 210, 0.7) 100%);
  }
  .contact {
    position: absolute;
    left: 40px;
    bottom: 46px;
    letter-spacing: 0.03em;
  }
  .contact__name { font-size: 21px; line-height: 1.15; }
  .contact__role { font-size: 17px; line-height: 1.2; opacity: 0.85; margin-bottom: 14px; }
  .contact__list { list-style: none; padding-left: 66px; font-size: 15px; line-height: 1.4; }
  .contact__label { display: inline-block; width: 44px; }

  /* Back */
  .card--back { background: var(--cream); color: var(--leaf-green); }
  .brand {
    position: absolute;
    left: 50%;
    top: 46%;
    transform: translate(-50%, -50%);
    display: flex;
    flex-direction: column;
    align-items: center;
    gap: 10px;
  }
  .brand__mark { width: 36px; height: 36px; border-radius: 50%; background: var(--leaf-green); }
  .brand__name { font-size: 23px; letter-spacing: 0.02em; }
  .abn {
    position: absolute;
    right: 30px;
    bottom: 74px;
    font-size: 15px;
    letter-spacing: 0.06em;
  }
</style>
</head>
<body>
  <main class="sheet">
    <section class="card card--front" aria-label="Business card front">
      <div class="figure-art" role="img" aria-label="Flat illustration of a woman's silhouette in a stone-grey dress, hands on hips"></div>
      <div class="contact">
        <p class="contact__name">Marta Solano</p>
        <p class="contact__role">Manager</p>
        <ul class="contact__list">
          <li><span class="contact__label">T.</span>+5057730-4812</li>
          <li><span class="contact__label">T.</span>+5053946-2087</li>
          <li><span class="contact__label">Mail.</span>msol48@mail.com</li>
        </ul>
      </div>
    </section>

    <section class="card card--back" aria-label="Business card back">
      <div class="brand">
        <span class="brand__mark"></span>
        <span class="brand__name">Plum Twist</span>
      </div>
      <p class="abn">ABN:&nbsp; 41027395816</p>
    </section>
  </main>
</body>
</html>
```